A5 Brochure for Vent Harbor
VENT HARBOR
Corporate and Residential
Logo of the certification/ Accreditation to be included into the brochure OEBX UPTKM GLO PKDV NEWB A5 Brochure front and back Pictures will be provided
Syarah Syarah
Hello, Could you please reopen the contest? Currently there're only 5 concepts to choose from. I hope you make the contest guaranteed, I think that would attract more designers to submit their concept. Regards.

```html
<!DOCTYPE html>
<html lang="en">
<head>
<meta charset="utf-8">
<title>Vent Harbor – A5 Brochure Layout</title>
<link href="https://fonts.googleapis.com/css2?family=Montserrat:wght@400;600;700&family=Open+Sans:wght@400;600&display=swap" rel="stylesheet">
<style>
  :root {
    --stage: #4a4a4a;
    --label: #d9d9d9;
    --paper: #ffffff;
    --brand-blue: #2f6fa8;
    --deep-blue: #1f5688;
    --light-blue: #6fa3cf;
    --accent-orange: #f07b2b;
    --body-grey: #7a7a7a;
    --rule-blue: #b9d2e8;
    --badge-grey: #d6d6d6;
  }
  * { margin: 0; padding: 0; box-sizing: border-box; }
  html, body { width: 1200px; height: 454px; overflow: hidden; background: var(--stage); }
  body { position: relative; font-family: "Montserrat", sans-serif; }

  .page-label {
    position: absolute; top: 12px;
    font-family: "Open Sans", sans-serif; font-size: 14px; color: var(--label);
  }
  .spec-note {
    position: absolute; top: 424px;
    font-family: "Open Sans", sans-serif; font-size: 12px; color: var(--label);
  }

  .page { position: absolute; background: var(--paper); overflow: hidden; }
  .front-page { left: 53px; top: 48px; width: 204px; height: 355px; }
  .back-page { left: 924px; top: 48px; width: 206px; height: 355px; }

  .spread {
    position: absolute; left: 372px; top: 41px; width: 434px; height: 369px;
    display: flex; box-shadow: 0 0 0 1px #3a3a3a;
  }
  .spread .page { position: relative; height: 369px; }
  .page-two { width: 216px; }
  .page-three { width: 218px; }

  .brand { position: absolute; left: 16px; top: 40px; }
  .brand-name {
    display: flex; align-items: center; gap: 5px;
    font-weight: 700; font-size: 19px; color: var(--brand-blue); letter-spacing: 0.3px;
  }
  .brand-mark { width: 13px; height: 13px; background: var(--brand-blue); flex: none; }
  .brand-tagline { margin-top: 2px; margin-left: 24px; font-size: 5.5px; color: var(--body-grey); letter-spacing: 0.3px; }

  .front-rule { position: absolute; left: 16px; top: 199px; width: 75px; height: 1px; background: var(--rule-blue); }
  .mission-panel {
    position: absolute; left: 91px; top: 199px; width: 113px; height: 137px;
    background: var(--brand-blue); color: #fff; padding: 28px 12px;
  }
  .mission-title { font-weight: 600; font-size: 12px; line-height: 1.15; }
  .mission-text { margin-top: 10px; font-size: 6.5px; line-height: 1.4; }

  .company-frame { position: absolute; left: 18px; top: 58px; width: 180px; height: 262px; border: 1px solid var(--rule-blue); }
  .company-photo {
    position: absolute; left: 0; top: 108px; width: 60px; height: 151px;
    background: linear-gradient(160deg, var(--light-blue), var(--deep-blue));
  }
  .company-copy { position: absolute; left: 74px; top: 122px; width: 116px; }
  .section-title { font-weight: 600; font-size: 12px; line-height: 1.15; color: var(--accent-orange); }
  .company-lead { margin-top: 6px; font-size: 4.8px; font-weight: 600; color: var(--brand-blue); }
  .company-body { margin-top: 4px; font-size: 4.8px; line-height: 1.5; color: var(--body-grey); }

  .services-photo {
    position: absolute; inset: 0;
    background: linear-gradient(150deg, #4f8cc2 0%, var(--brand-blue) 50%, var(--deep-blue) 100%);
  }
  .services-box {
    position: absolute; left: 47px; top: 122px; width: 168px; height: 137px;
    border: 1px solid #fff; color: #fff; padding: 10px 10px;
  }
  .services-title { font-weight: 600; font-size: 10px; letter-spacing: 0.5px; padding-bottom: 6px; border-bottom: 1px solid rgba(255,255,255,0.7); }
  .services-list { list-style: none; margin-top: 10px; font-size: 7px; line-height: 2.1; font-family: "Open Sans", sans-serif; }
  .services-list span { display: inline-block; width: 13px; }

  .contact-copy { position: absolute; left: 16px; top: 128px; width: 182px; }
  .contact-list { list-style: none; margin-top: 10px; font-size: 5px; line-height: 1.75; color: var(--body-grey); }
  .badge-row { position: absolute; left: 16px; top: 286px; display: flex; gap: 8px; align-items: center; }
  .badge { width: 28px; height: 20px; background: var(--badge-grey); }
  .badge.round { width: 20px; height: 20px; border-radius: 50%; }
</style>
</head>
<body>
  <div class="page-label" style="left:117px">Front page</div>
  <div class="page-label" style="left:462px">Page 2</div>
  <div class="page-label" style="left:664px">Page 3</div>
  <div class="page-label" style="left:996px">Back page</div>

  <section class="page front-page">
    <div class="brand">
      <div class="brand-name"><span class="brand-mark"></span>VENT HARBOR</div>
      <div class="brand-tagline">Investigate | Remediate | Control</div>
    </div>
    <div class="front-rule"></div>
    <div class="mission-panel">
      <div class="mission-title">OUR<br>MISSION</div>
      <div class="mission-text">Investigate, Eliminate<br>and Control</div>
    </div>
  </section>

  <div class="spread">
    <section class="page page-two">
      <div class="company-frame"></div>
      <div class="company-photo" role="img" aria-label="Photo of a technician inspecting a home interior"></div>
      <div class="company-copy">
        <div class="section-title">OUR<br>COMPANY</div>
        <div class="company-lead">HEALTHY HOMES &amp; CLEAN AIR SPECIALISTS</div>
        <p class="company-body">We help families and businesses find, remove and prevent damp and mould. Our certified team uses proven methods to restore safe indoor air and protect every building we treat.</p>
      </div>
    </section>
    <section class="page page-three">
      <div class="services-photo" role="img" aria-label="Blue tinted photo of a remediation worker on site"></div>
      <div class="services-box">
        <div class="services-title">WHAT WE DO</div>
        <ul class="services-list">
          <li><span>01</span>Mould Remediation</li>
          <li><span>02</span>Indoor Air Quality Assessment</li>
          <li><span>03</span>Building Assessment (BA)</li>
          <li><span>04</span>Post Remediation Verification</li>
        </ul>
      </div>
    </section>
  </div>

  <section class="page back-page">
    <div class="brand">
      <div class="brand-name"><span class="brand-mark"></span>VENT HARBOR</div>
      <div class="brand-tagline">Investigate | Remediate | Control</div>
    </div>
    <div class="contact-copy">
      <div class="section-title">OUR<br>CONTACTS</div>
      <ul class="contact-list">
        <li>Phone: 1 555 014 270</li>
        <li>Email: hello@ventharbor.example</li>
        <li>Unit 4/12 Harbour Road, Westvale, NS 2150</li>
        <li>Website: www.ventharbor.example</li>
        <li>social.example/ventharbor</li>
      </ul>
    </div>
    <div class="badge-row" aria-label="Accreditation badges">
      <div class="badge"></div>
      <div class="badge"></div>
      <div class="badge round"></div>
      <div class="badge round"></div>
      <div class="badge round"></div>
    </div>
  </section>

  <div class="spec-note" style="left:348px">Each page is format A5: 148mm x 210mm</div>
  <div class="spec-note" style="left:672px">2 Color Print on white paper</div>
  <div class="spec-note" style="left:893px">3 pictures used</div>
</body>
</html>
```